Commercial Real Estate Executive Recruiting Firm Needs Business Card Design

We need a business card design for BRAMLEY | Executive Recruiting - an executive recruiting firm focused exclusively on the commercial real estate industry. We place professionals ranging from Analyst to the Executive Office covering all investment/finance disciplines (acquisitions, asset management, capital markets, etc.) in all product types (office, retail, multifamily, industrial, land, etc.). We have a passion for helping people (clients and candidates) and have a reputation for being open and honest in our recruiting - and yes, very successful. We have recently developed a new logo and would like to update our business cards as well. I've uploaded some information about our company that contains the new logo.

Target Market(s)

Commercial Real Estate professionals. Primarily in the US. These are typically, smart, driven professionals with finance degrees and MBAs. Primarily men between the ages of 25 and 55.

Industry/Entity Type

Real Estate

Font styles to use
Other font styles liked:
• The font for "BRAMLEY" is Blair ITC (Medium), and "executive recruiting" is Gotham (Book).

Requirements
Must have
• I like the idea of white background on one side and solid color (blue, black, etc.) on back of card.

Would like to utilize the fonts in the logo (to the extent possible) so as to not have too many fonts on card.
Nice to have
• I think the roles (i.e., Acquisitions, Asset Management, etc.,...) is probably likely best placed on the back side of the card with the logo maybe. See attached current business card for content.

```html
<!DOCTYPE html>
<html lang="en">
<head>
<meta charset="utf-8">
<title>BRAMLEY | Executive Recruiting — Business Card</title>
<link rel="stylesheet" href="https://fonts.googleapis.com/css2?family=Michroma&family=Montserrat:wght@400;500&family=Open+Sans:wght@600;700;800&display=swap">
<style>
  :root {
    --canvas: #e9e7e3;
    --card-white: #f7f7f5;
    --brand-blue: #2b7bc4;
    --navy: #16314f;
    --ink: #3a3a3a;
    --grey: #6b6b6b;
    --strip: #ffffff;
  }
  * { box-sizing: border-box; margin: 0; padding: 0; }
  html, body { width: 1200px; height: 857px; overflow: hidden; }
  body {
    background: var(--canvas);
    font-family: "Open Sans", sans-serif;
    position: relative;
  }
  .card {
    position: absolute;
    left: 300px;
    width: 600px;
    height: 343px;
    overflow: hidden;
    box-shadow: 0 6px 18px rgba(0,0,0,0.18);
  }

  /* Back of card */
  .card--back { top: 40px; background: var(--brand-blue); }
  .back-mark {
    position: absolute;
    left: 0; right: 0; top: 120px;
    display: flex; align-items: center; justify-content: center; gap: 18px;
    color: rgba(255,255,255,0.82);
  }
  .back-mark .mark-square { width: 46px; height: 46px; background: rgba(255,255,255,0.82); }
  .back-mark .wordmark { font-family: "Michroma", sans-serif; font-size: 38px; letter-spacing: 8px; }
  .role-strip {
    position: absolute; left: 0; right: 0; bottom: 0;
    height: 30px; background: var(--strip);
    display: flex; align-items: center; justify-content: center;
    font-size: 11.5px; font-weight: 800; color: var(--navy); letter-spacing: 0.4px;
    white-space: nowrap;
  }

  /* Front of card */
  .card--front { top: 423px; background: var(--card-white); }
  .edge-top {
    position: absolute; top: 0; left: 0; width: 220px; height: 7px; background: var(--navy);
  }
  .edge-top::after {
    content: ""; position: absolute; left: 220px; top: 0; width: 380px; height: 3px; background: var(--brand-blue);
  }
  .edge-bottom { position: absolute; left: 0; right: 0; bottom: 0; height: 8px; background: var(--brand-blue); }
  .edge-bottom::before { content: ""; position: absolute; left: 0; top: 0; width: 110px; height: 8px; background: var(--navy); }

  .logo { position: absolute; top: 34px; left: 34px; display: flex; align-items: flex-start; gap: 12px; }
  .logo .mark-square { width: 34px; height: 34px; background: var(--navy); }
  .logo .wordmark {
    font-family: "Michroma", sans-serif; font-size: 27px; letter-spacing: 7px; color: var(--ink); line-height: 1;
  }
  .logo .tagline {
    font-family: "Montserrat", sans-serif; font-size: 14px; letter-spacing: 2.4px; color: var(--grey); margin-top: 6px;
  }

  .website {
    position: absolute; top: 118px; right: 34px;
    font-size: 15px; font-weight: 600; color: var(--brand-blue); letter-spacing: 1.4px;
  }
  .identity { position: absolute; right: 34px; top: 210px; text-align: right; }
  .identity .name { font-size: 30px; font-weight: 800; color: var(--navy); letter-spacing: 2px; }
  .identity .title { font-size: 14px; font-weight: 700; color: var(--brand-blue); letter-spacing: 3px; }

  .contact { position: absolute; left: 34px; bottom: 28px; font-size: 14px; font-weight: 600; color: var(--navy); letter-spacing: 0.8px; line-height: 1.9; }
  .contact .label { color: var(--brand-blue); font-weight: 800; }
</style>
</head>
<body>

  <section class="card card--back" aria-label="Back of business card">
    <div class="back-mark">
      <span class="mark-square"></span>
      <span class="wordmark">BRAMLEY</span>
    </div>
    <div class="role-strip">Acquisitions | Asset Management | Banking | Development | Capital Markets | Brokerage</div>
  </section>

  <section class="card card--front" aria-label="Front of business card">
    <div class="edge-top"></div>
    <div class="logo">
      <span class="mark-square"></span>
      <div>
        <div class="wordmark">BRAMLEY</div>
        <div class="tagline">executive recruiting</div>
      </div>
    </div>
    <div class="website">www.bramleyrecruiting.com</div>
    <div class="identity">
      <div class="name">Jordan Hale</div>
      <div class="title">PRESIDENT</div>
    </div>
    <div class="contact">
      <div><span class="label">M |</span> 214-555-0148</div>
      <div><span class="label">E |</span> jordan@bramleyrecruiting.com</div>
    </div>
    <div class="edge-bottom"></div>
  </section>

</body>
</html>
```